2 sets of Business cards, stationary/envelopes, stationary template(MS Word), door hang tag
KRV Building Works, LLC (Design A) and Steadfield Estate Holdings, LLC (Design B)
2 sets of Business cards, stationary/envelopes, stationary template(MS Word), door hang tag - Real Estate
Creative Brief
Simple
Darrel K. Winton
Managing Member
5120 Larkspur Lane, Suite B Columbia, MO 65201
Don't know yet, but need space for it
dwinton@krvbuildworks.com
www.krvbuildworks.com (Design A) and www.steadfieldleasing.com (Design B)
We are a family owned business with 90+ years in the construction and real estate sector and would like to present our company as a quality, professional organization with a sleek modern set of stationary. Stationary design A: Company name: KRV Building Works, LLC Optional Tagline: Working from experience, not for it! Color Mode: RGB color Grey :R=149 G=149 B=149 White: R=255 G=255 B=255 Black : R=0 G=0 B=0 Blue : R=0 G=97 B=240 dwinton@krvbuildworks.com (Design A) For: KRV Building Works, LLC Stationary design B: Company name: Steadfield Estate Holdings, LLC Optional Tagline: Steadfield Precision, Steadfield Dedication Color Mode: RGB color Grey :R=149 G=149 B=149 White: R=255 G=255 B=255 Black : R=0 G=0 B=0 Red : R=209 G=0 B=0 dwinton@steadfieldleasing.com (Design B) For: Steadfield Estate Holdings, LLC Phone, email, and name will change for the additional members of the company. We also want an electronic email signature, and digital stationary template (MS word). Stationary and envelopes should tie in the theme of the business cards for a uniform look. Also looking for a Header only version of the stationary, as well as a full page version (header and footer used for design).
Logo used in a creative way.
darrelkwinton darrelkwinton
Sorry, been out of the office. Waiting for partners to look at everything before making comments. We should be leaving comments and making recommendations in the next day or two for all of the designs we want to see refined. Thanks, Darrel

```html
<!DOCTYPE html>
<html lang="en">
<head>
<meta charset="utf-8">
<title>KRV Building Works &amp; Steadfield Estate Holdings — Stationery Set</title>
<link rel="stylesheet" href="https://fonts.googleapis.com/css2?family=Open+Sans:wght@400;700&display=swap">
<style>
  :root{
    --stage:#3d3d3d;
    --paper:#ffffff;
    --ink:#000000;
    --grey:#959595;
    --blue:#0061f0;
    --red:#d10000;
    --card-back:#161616;
  }
  *{box-sizing:border-box;margin:0;padding:0}
  html,body{width:1200px;height:404px;overflow:hidden;background:var(--stage);font-family:"Open Sans",Arial,sans-serif}
  .canvas{position:relative;width:1200px;height:404px}
  .piece{position:absolute;background:var(--paper);overflow:hidden;box-shadow:0 1px 3px rgba(0,0,0,.45)}
  .piece svg.wave{position:absolute;left:0;bottom:0;width:100%;height:100%}
  .brand{position:absolute;display:flex;align-items:center;gap:3px;line-height:1;white-space:nowrap}
  .brand-dot{border-radius:50%;flex:none}
  .brand-name{display:block;font-weight:700}
  .brand-sub{display:block;font-weight:400;color:var(--grey);margin-top:1px}
  .theme-blue .brand-dot{background:var(--blue)}
  .theme-blue .brand-name{color:var(--blue)}
  .theme-red .brand-dot{background:var(--red)}
  .theme-red .brand-name{color:var(--red)}
  .contact{position:absolute;color:#333;line-height:1.35;white-space:nowrap}
  .contact strong{display:block;color:var(--ink)}
  /* small business cards */
  .card-small{width:98px;height:52px}
  .card-small .brand{left:6px;top:9px}
  .card-small .brand-dot{width:6px;height:6px}
  .card-small .brand-name{font-size:7px}
  .card-small .brand-sub{font-size:3px}
  .card-back{background:var(--card-back)}
  .card-back .back-fill{position:absolute;inset:0;background:linear-gradient(135deg,#1f1f1f,#0c0c0c)}
  /* large business cards */
  .card-large{width:144px;height:62px}
  .card-large .brand{left:7px;top:10px}
  .card-large .brand-dot{width:8px;height:8px}
  .card-large .brand-name{font-size:9px}
  .card-large .brand-sub{font-size:3.5px}
  .card-large .contact{left:82px;top:11px;font-size:3.5px}
  /* letterheads */
  .letterhead{width:238px;height:312px}
  .letterhead .brand{left:14px;top:16px}
  .letterhead .brand-dot{width:11px;height:11px}
  .letterhead .brand-name{font-size:13px}
  .letterhead .brand-sub{font-size:4.5px}
  .letterhead .emblem{position:absolute;left:95px;top:128px;width:48px;height:48px;border-radius:50%;background:#ececec}
  .letterhead .contact{left:14px;bottom:8px;font-size:3.5px;color:#cfcfcf}
  .letterhead .contact strong{color:#fff}
  /* envelopes */
  .envelope{width:250px;height:116px}
  .envelope .brand{left:10px;top:12px}
  .envelope .brand-dot{width:10px;height:10px}
  .envelope .brand-name{font-size:12px}
  .envelope .brand-sub{font-size:4px}
  .envelope .contact{left:10px;top:34px;font-size:3.5px}
  .envelope-back svg{position:absolute;inset:0;width:100%;height:100%}
  .envelope-back .seal{position:absolute;left:120px;top:49px;width:10px;height:10px;border-radius:50%;border:2px solid var(--paper)}
  .theme-blue .seal{background:var(--blue)}
  .theme-red .seal{background:var(--red)}
</style>
</head>
<body>
<main class="canvas">

  <!-- Business cards, left column -->
  <section class="piece card-small theme-blue" style="left:34px;top:79px">
    <svg class="wave" viewBox="0 0 100 52" preserveAspectRatio="none" aria-hidden="true">
      <path d="M0 40 C30 30 60 48 100 30 L100 52 L0 52Z" fill="var(--ink)"/>
      <path d="M0 38 C30 28 60 46 100 28" fill="none" stroke="var(--blue)" stroke-width="1.6"/>
    </svg>
    <div class="brand"><span class="brand-dot"></span><div><span class="brand-name">KRV</span><span class="brand-sub">Building Works, LLC</span></div></div>
  </section>
  <section class="piece card-small card-back" style="left:34px;top:144px">
    <div class="back-fill" role="img" aria-label="Dark textured card back pattern"></div>
  </section>
  <section class="piece card-small theme-red" style="left:34px;top:216px">
    <svg class="wave" viewBox="0 0 100 52" preserveAspectRatio="none" aria-hidden="true">
      <path d="M0 40 C30 30 60 48 100 30 L100 52 L0 52Z" fill="var(--ink)"/>
      <path d="M0 38 C30 28 60 46 100 28" fill="none" stroke="var(--red)" stroke-width="1.6"/>
    </svg>
    <div class="brand"><span class="brand-dot"></span><div><span class="brand-name">Steadfield</span><span class="brand-sub">Estate Holdings, LLC</span></div></div>
  </section>
  <section class="piece card-small card-back" style="left:34px;top:281px">
    <div class="back-fill" role="img" aria-label="Dark textured card back pattern"></div>
  </section>

  <!-- Letterheads -->
  <section class="piece letterhead theme-blue" style="left:144px;top:53px">
    <div class="brand"><span class="brand-dot"></span><div><span class="brand-name">KRV</span><span class="brand-sub">Building Works, LLC</span></div></div>
    <div class="emblem" aria-hidden="true"></div>
    <svg class="wave" viewBox="0 0 100 130" preserveAspectRatio="none" aria-hidden="true">
      <path d="M0 119 C30 110 60 124 100 105 L100 130 L0 130Z" fill="var(--ink)"/>
      <path d="M0 117 C30 108 60 122 100 103" fill="none" stroke="var(--grey)" stroke-width="0.6"/>
      <path d="M0 118 C30 109 60 123 100 104" fill="none" stroke="var(--blue)" stroke-width="0.9"/>
    </svg>
    <div class="contact"><strong>5120 Larkspur Lane, Suite B Columbia, MO 65201</strong>dwinton@krvbuildworks.com · www.krvbuildworks.com</div>
  </section>
  <section class="piece letterhead theme-blue" style="left:391px;top:53px">
    <div class="brand"><span class="brand-dot"></span><div><span class="brand-name">KRV</span><span class="brand-sub">Building Works, LLC</span></div></div>
    <div class="emblem" aria-hidden="true"></div>
    <svg class="wave" viewBox="0 0 100 130" preserveAspectRatio="none" aria-hidden="true">
      <path d="M0 119 C30 110 60 124 100 105 L100 130 L0 130Z" fill="var(--ink)"/>
      <path d="M0 117 C30 108 60 122 100 103" fill="none" stroke="var(--grey)" stroke-width="0.6"/>
      <path d="M0 118 C30 109 60 123 100 104" fill="none" stroke="var(--blue)" stroke-width="0.9"/>
    </svg>
    <div class="contact"><strong>5120 Larkspur Lane, Suite B Columbia, MO 65201</strong>dwinton@krvbuildworks.com · www.krvbuildworks.com</div>
  </section>

  <!-- Large business cards -->
  <section class="piece card-large theme-blue" style="left:696px;top:34px">
    <svg class="wave" viewBox="0 0 144 62" preserveAspectRatio="none" aria-hidden="true">
      <path d="M0 48 C45 38 90 58 144 38 L144 62 L0 62Z" fill="var(--ink)"/>
      <path d="M0 46 C45 36 90 56 144 36" fill="none" stroke="var(--blue)" stroke-width="2"/>
    </svg>
    <div class="brand"><span class="brand-dot"></span><div><span class="brand-name">KRV</span><span class="brand-sub">Building Works, LLC</span></div></div>
    <div class="contact"><strong>Darrel K. Winton</strong>Managing Member<br>(573) 555-0142<br>dwinton@krvbuildworks.com</div>
  </section>
  <section class="piece card-large theme-red" style="left:960px;top:34px">
    <svg class="wave" viewBox="0 0 144 62" preserveAspectRatio="none" aria-hidden="true">
      <path d="M0 48 C45 38 90 58 144 38 L144 62 L0 62Z" fill="var(--ink)"/>
      <path d="M0 46 C45 36 90 56 144 36" fill="none" stroke="var(--red)" stroke-width="2"/>
    </svg>
    <div class="brand"><span class="brand-dot"></span><div><span class="brand-name">Steadfield</span><span class="brand-sub">Estate Holdings, LLC</span></div></div>
    <div class="contact"><strong>Darrel K. Winton</strong>Managing Member<br>(573) 555-0187<br>dwinton@steadfieldleasing.com</div>
  </section>

  <!-- Envelopes -->
  <section class="piece envelope theme-blue" style="left:643px;top:115px">
    <svg class="wave" viewBox="0 0 250 116" preserveAspectRatio="none" aria-hidden="true">
      <path d="M0 100 C80 86 150 110 250 70 L250 116 L0 116Z" fill="var(--ink)"/>
      <path d="M0 97 C80 83 150 107 250 67" fill="none" stroke="var(--blue)" stroke-width="2.4"/>
    </svg>
    <div class="brand"><span class="brand-dot"></span><div><span class="brand-name">KRV</span><span class="brand-sub">Building Works, LLC</span></div></div>
    <div class="contact">5120 Larkspur Lane, Suite B<br>Columbia, MO 65201</div>
  </section>
  <section class="piece envelope envelope-back theme-blue" style="left:907px;top:115px">
    <svg viewBox="0 0 250 116" preserveAspectRatio="none" aria-hidden="true">
      <path d="M0 0 L250 0 L250 8 L125 58 L0 8Z" fill="var(--ink)"/>
    </svg>
    <span class="seal" aria-hidden="true"></span>
  </section>
  <section class="piece envelope theme-red" style="left:643px;top:248px">
    <svg class="wave" viewBox="0 0 250 116" preserveAspectRatio="none" aria-hidden="true">
      <path d="M0 100 C80 86 150 110 250 70 L250 116 L0 116Z" fill="var(--ink)"/>
      <path d="M0 97 C80 83 150 107 250 67" fill="none" stroke="var(--red)" stroke-width="2.4"/>
    </svg>
    <div class="brand"><span class="brand-dot"></span><div><span class="brand-name">Steadfield</span><span class="brand-sub">Estate Holdings, LLC</span></div></div>
    <div class="contact">5120 Larkspur Lane, Suite B<br>Columbia, MO 65201</div>
  </section>
  <section class="piece envelope envelope-back theme-red" style="left:907px;top:248px">
    <svg viewBox="0 0 250 116" preserveAspectRatio="none" aria-hidden="true">
      <path d="M0 0 L250 0 L250 8 L125 58 L0 8Z" fill="var(--ink)"/>
    </svg>
    <span class="seal" aria-hidden="true"></span>
  </section>

</main>
</body>
</html>
```